Gigmarket Messenger Android App Mockup

I need a mockup of a possible Android Gigmarket messenger app for Gigmarket.net

The mockup only needs to be a single screen, showing a message thread between 2 users (Ie where users will actually 'chat' - see attached jpeg for an equivalent screen in a different app)

The mockup should be based around the general Gigmarket colour scheme and should look like a modern Android app. Besides that be as creative as you like!

```html
<!DOCTYPE html>
<html lang="en">
<head>
<meta charset="utf-8">
<title>Gigmarket Messenger</title>
<link href="https://fonts.googleapis.com/css2?family=Arimo:ital,wght@0,400;0,700;1,700&display=swap" rel="stylesheet">
<style>
:root{
  --page:#ffffff;
  --status:#111111;
  --header:#2f3134;
  --header-top:#4a4d51;
  --tab-active:#2a9ad8;
  --tab-idle:#34363a;
  --chat-top:#cfe4f4;
  --chat-mid:#f4f9fd;
  --chat-bottom:#c4def1;
  --orange:#f08a1c;
  --blue:#2a8fe0;
  --green:#2f9a2a;
  --ink:#1a1a1a;
  --tick:#2a8fe0;
  --input-bar:#3a3c3f;
  --arrow:#6aa9dc;
  --parcel:#e2a64a;
}
*{margin:0;padding:0;box-sizing:border-box}
html,body{width:1200px;height:675px;overflow:hidden;background:var(--page);font-family:"Arimo",Arial,sans-serif}
.screen{position:absolute;left:408px;top:0;width:384px;height:675px;overflow:hidden}
.status-bar{height:27px;background:var(--status);display:flex;align-items:center;justify-content:flex-end;gap:8px;padding:0 10px;color:#fff;font-size:15px}
.status-bar .dot{width:10px;height:12px;background:#6bbf3a;border-radius:2px}
.status-bar .left{margin-right:auto;display:flex;gap:6px}
.app-header{height:49px;background:linear-gradient(var(--header-top),var(--header));display:flex;align-items:center;padding:0 12px;position:relative}
.brand{display:flex;align-items:center;gap:8px;color:#fff;font-weight:700;font-size:24px}
.brand-mark{width:16px;height:16px;border-radius:50%;background:var(--tab-active)}
.attach{position:absolute;right:0;top:0;width:56px;height:49px;border-left:1px solid #555;display:flex;align-items:center;justify-content:center}
.tabs{height:33px;display:flex}
.tab{flex:1;display:flex;align-items:center;justify-content:center;color:#fff;font-size:25px;background:var(--tab-idle)}
.tab.active{background:var(--tab-active)}
.thread{position:relative;height:515px;background:linear-gradient(var(--chat-top),var(--chat-mid) 45%,var(--chat-bottom))}
.bubble{position:absolute;border:5px solid;border-radius:8px;background:#fff;padding:6px 12px 8px}
.bubble::before{content:"";position:absolute;top:18px;border:10px solid transparent}
.bubble.in::before{left:-24px;border-right-color:inherit}
.bubble.out::before{right:-24px;border-left-color:inherit}
.bubble.orange{border-color:var(--orange)}
.bubble.blue{border-color:var(--blue)}
.bubble.green{border-color:var(--green)}
.sender{font-weight:700;font-size:26px;line-height:30px}
.orange .sender{color:var(--orange)}
.blue .sender{color:var(--blue)}
.text{font-weight:700;font-style:italic;font-size:15px;line-height:19px;color:var(--ink)}
.row{display:flex;align-items:center;justify-content:space-between;gap:10px;min-height:20px}
.time{font-size:15px;line-height:19px;color:var(--ink);display:flex;align-items:center;gap:5px;margin-left:auto;white-space:nowrap}
.divider{height:1px;background:var(--blue);width:150px}
.scroll{position:absolute;left:341px;width:32px;height:32px;border-radius:50%;border:2px solid var(--arrow);background:#e9f3fb;display:flex;align-items:center;justify-content:center}
.parcel{position:absolute;left:328px;top:160px;width:44px;height:44px;border-radius:6px;background:linear-gradient(#f2c677,var(--parcel))}
.composer{height:51px;background:var(--input-bar);display:flex;align-items:center;padding:0 8px;gap:10px}
.emoji{width:32px;height:32px;border-radius:50%;background:#fff}
.field{flex:1;height:34px;background:#fff;border:2px solid #9aa}
.send{width:40px;height:40px;display:flex;align-items:center;justify-content:center}
</style>
</head>
<body>
<main class="screen">
  <div class="status-bar">
    <span class="left"><span class="dot"></span><span class="dot"></span></span>
    <span>4:12 PM</span>
  </div>
  <header class="app-header">
    <div class="brand"><span class="brand-mark"></span>Gigmarket.net</div>
    <div class="attach">
      <svg width="26" height="34" viewBox="0 0 26 34"><path d="M8 24V8a5 5 0 0 1 10 0v18a8 8 0 0 1-16 0V10" fill="none" stroke="#fff" stroke-width="2.4" stroke-linecap="round"/></svg>
    </div>
  </header>
  <nav class="tabs"><div class="tab active">Contest</div><div class="tab">Project</div></nav>

  <section class="thread">
    <div class="scroll" style="top:13px"><svg width="18" height="12" viewBox="0 0 18 12"><path d="M2 10 9 3l7 7" fill="none" stroke="var(--arrow)" stroke-width="3"/></svg></div>

    <article class="bubble in orange" style="left:16px;top:13px;width:303px">
      <div class="sender">Marawinslow</div>
      <p class="text">This discussion is giving me new ideas</p>
      <div class="row"><span class="time">3:45 pm <svg width="18" height="12" viewBox="0 0 18 12"><path d="M1 6l5 5L17 1" fill="none" stroke="var(--tick)" stroke-width="2"/></svg></span></div>
    </article>

    <article class="bubble in blue" style="left:16px;top:137px;width:303px">
      <div class="sender">Tomcrafter123</div>
      <p class="text">Here is the work I just finished...</p>
      <div class="row"><span class="text">Hope you like it</span><span class="time">3:54 pm <svg width="18" height="12" viewBox="0 0 18 12"><path d="M1 6l5 5L17 1" fill="none" stroke="var(--tick)" stroke-width="2"/></svg></span></div>
    </article>
    <div class="parcel" role="img" aria-label="Attached file parcel icon"></div>

    <article class="bubble out green" style="left:62px;top:264px;width:302px">
      <p class="text">Oh yeah, thank you for the entry tomcrafter123, i will rate it soon..</p>
      <div class="row"><span class="divider"></span><span class="time">4:01 pm <svg width="18" height="12" viewBox="0 0 18 12"><path d="M1 6l5 5L17 1" fill="none" stroke="var(--tick)" stroke-width="2"/></svg></span></div>
      <div class="row"><span class="text">i like it...</span><span class="time">4:10 pm <svg width="18" height="12" viewBox="0 0 18 12"><path d="M1 6l5 5L17 1" fill="none" stroke="var(--tick)" stroke-width="2"/></svg></span></div>
    </article>

    <article class="bubble in blue" style="left:16px;top:410px;width:303px">
      <div class="sender">Tomcrafter123</div>
      <p class="text">Okay, thank you</p>
      <div class="row" style="margin-top:4px"><span class="time">4:12 pm</span></div>
    </article>

    <div class="scroll" style="top:463px"><svg width="18" height="12" viewBox="0 0 18 12"><path d="M2 2l7 7 7-7" fill="none" stroke="var(--arrow)" stroke-width="3"/></svg></div>
  </section>

  <footer class="composer">
    <span class="emoji"></span>
    <span class="field"></span>
    <span class="send"><svg width="32" height="28" viewBox="0 0 32 28"><path d="M2 2l28 12L2 26l5-12z" fill="var(--arrow)"/></svg></span>
  </footer>
</main>
</body>
</html>
```